Harbor Geriatric care need Business card design

Simple and elegance looking business card (colour choice will be very important)
Harbor geriatric care is medical consultation service for elderly population.

1st side---business logo and the doctor name/tile
eg: dr. XXX
MBBS,FRACP etc
Main room:
suite xxx AAA medical centre 18 XXX road Vic 3000
Phone:
Fax:

2nd side --different clinic address (up to 3 addresses) and need to have appointment time/ date

Suite xxx AAA medical centre , 18 XXX road VIC 3000

Please see attachment for business logo

Important: need to be compatible with Marlo Press for printing purpose.

Thank you.

hi, please look at the sample business card and create something similar. Company name: Harbor Geriatric Care PTY LTD ABN 47690518 ( all small font and no need to be obvious) company logo need to be obvious Apart from steady in support, also add Geriatrician for Community and Residential Care. Main room Dunova Medical Centre suite 2.14 204-206 Pelling street Box Hill Vic All appointment and enquiries: tel: 947160258 Fasmile: www.qwxplomz.com.au Kellwyn Medical Centre 42 dunmore road kellwyn VIC Ridgefield Care Frankston 587 Pellham road , franskton VIC 3199 Orchard Private Hospital specialist room 264 Tollard Road, Mt. Orchard VIC 3333 Dr. PN 80917kt DR. HW r8026179mm DR. GT 907612mm Thank you

```html
<!DOCTYPE html>
<html lang="en">
<head>
<meta charset="utf-8">
<title>Harbor Geriatric Care – Business Card</title>
<link rel="stylesheet" href="https://fonts.googleapis.com/css2?family=Roboto+Condensed:ital,wght@0,400;0,700;1,400;1,700&display=swap">
<style>
  :root {
    --bg: #e9e9e9;
    --card: #ffffff;
    --red: #c0202f;
    --red-dark: #a8141f;
    --navy: #27336b;
    --grey: #6a6a6a;
    --rule: #7a7a7a;
  }
  * { margin: 0; padding: 0; box-sizing: border-box; }
  html, body { width: 1200px; height: 720px; overflow: hidden; background: var(--bg); }
  body { position: relative; font-family: "Roboto Condensed", Arial, sans-serif; color: var(--grey); }

  .card { position: absolute; top: 241px; width: 420px; height: 240px; background: var(--card); overflow: hidden; }
  .card--front { left: 147px; }
  .card--back { left: 633px; }

  /* Front */
  .abn { position: absolute; left: 24px; top: 17px; font-size: 10px; font-weight: 700; color: var(--grey); }
  .brand { position: absolute; left: 20px; top: 46px; width: 170px; text-align: center; }
  .brand__mark { display: block; margin: 0 auto 14px; }
  .brand__name { font-size: 17px; font-weight: 700; color: var(--navy); white-space: nowrap; line-height: 1; }
  .brand__tagline { margin-top: 3px; font-size: 5.5px; letter-spacing: 2.6px; color: var(--grey); text-transform: uppercase; }

  .doctor { position: absolute; left: 207px; top: 34px; font-size: 10px; line-height: 14.5px; }
  .doctor__name { color: var(--red); font-weight: 700; }
  .doctor__block { margin-top: 14.5px; }
  .contact-row { display: flex; }
  .contact-row__label { width: 40px; }
  .contact-row__sep { width: 14px; }

  .front-band { position: absolute; left: 0; bottom: 0; width: 100%; height: 42px; background: linear-gradient(90deg, var(--red-dark), var(--red)); color: #fff; text-align: center; font-size: 9.6px; line-height: 12px; padding-top: 2px; }
  .front-band p:first-child { font-weight: 700; }

  /* Back */
  .appointment { position: absolute; left: 0; width: 196px; border-bottom: 1px solid var(--rule); padding-left: 29px; font-size: 9.6px; font-style: italic; font-weight: 700; color: var(--red); line-height: 12px; }
  .appointment--1 { top: 71px; }
  .appointment--2 { top: 107px; }
  .appointment--3 { top: 142px; }

  .clinics { position: absolute; left: 209px; top: 44px; font-size: 9.6px; font-style: italic; line-height: 11.6px; color: var(--grey); }
  .clinic + .clinic { margin-top: 11.6px; }
  .clinic__name { font-weight: 700; }

  .back-band { position: absolute; left: 0; bottom: 0; width: 100%; height: 13px; background: linear-gradient(90deg, var(--red), var(--red-dark)); }
</style>
</head>
<body>
  <section class="card card--front">
    <p class="abn">ABN 47690518</p>

    <div class="brand">
      <svg class="brand__mark" width="110" height="110" viewBox="0 0 110 110" aria-hidden="true">
        <circle cx="55" cy="55" r="52" fill="var(--red)"/>
      </svg>
      <p class="brand__name">Harbor Geriatric Care</p>
      <p class="brand__tagline">Steady in support</p>
    </div>

    <div class="doctor">
      <p class="doctor__name">Dr. MARTIN KEEL</p>
      <p>Consultant physician and Geriatrician</p>
      <p>MBBS, FRACP, Clin Dip Pall Care</p>
      <div class="doctor__block">
        <p>Main room:</p>
        <p>Suite 2.14, Level 2, Dunova Medical Box Hill</p>
        <p>204-206 Pelling Street, Box Hill, VIC 3128</p>
      </div>
      <div class="doctor__block">
        <p class="contact-row"><span class="contact-row__label">Phone</span><span class="contact-row__sep">:</span><span>46218093</span></p>
        <p class="contact-row"><span class="contact-row__label">Fax</span><span class="contact-row__sep">:</span><span>73159024</span></p>
      </div>
    </div>

    <div class="front-band">
      <p>Geriatrician for Community and Residential Care</p>
      <p>All Appointment and Enquiries: Telephone: 947160258 Fasmile: www.qwxplomz.com.au</p>
    </div>
  </section>

  <section class="card card--back">
    <p class="appointment appointment--1">Dr. PN 80917kt</p>
    <p class="appointment appointment--2">Dr. HW r8026179mm</p>
    <p class="appointment appointment--3">Dr. GT 907612mm</p>

    <div class="clinics">
      <div class="clinic">
        <p class="clinic__name">Orchard Private Hospital Consulting Suites</p>
        <p>318-332 Tollard Road</p>
        <p>Mt. Orchard Vic 3149</p>
        <p>Phone: (03) 9460 2215</p>
      </div>
      <div class="clinic">
        <p class="clinic__name">Ridgefield Care Frankston</p>
        <p>571-581 Pellham Road</p>
        <p>Frankston 3199</p>
        <p>Phone: (03) 9715 4820</p>
      </div>
      <div class="clinic">
        <p class="clinic__name">Kellwyn Medical Centre</p>
        <p>42 Dunmore road</p>
        <p>Kellwyn VIC</p>
      </div>
    </div>

    <div class="back-band"></div>
  </section>
</body>
</html>
```